PowerPoint Design Project

I need a Power Point slide template designed with 4 or 5 slides. We are a health care technology company and would like to take our current look and feel in this PP presentation to the next level and "prettied up"

Target Market(s)

Health Care Professionals

Industry/Entity Type

Health

Requirements
Must have
• Cannot change out the TOLVARE logo. The logo is all CAPS
Should not have
• The color blue is restricted and cannot be used.

```html
<!DOCTYPE html>
<html lang="en">
<head>
<meta charset="utf-8">
<title>Project Title Here</title>
<link rel="stylesheet" href="https://fonts.googleapis.com/css2?family=Ubuntu:wght@400;700&family=Carlito&family=Roboto+Condensed:wght@700&display=swap">
<style>
  :root {
    --lime: #b2bb23;
    --white: #ffffff;
    --ink: #2b2b20;
    --brand-grey: #9a9a9a;
    --footer-top: #f4f4f4;
    --footer-bottom: #d6d6d6;
    --footer-line: #c8c8c8;
    --dots: #e6e6e6;
  }
  html, body {
    margin: 0;
    padding: 0;
    width: 1200px;
    height: 900px;
    overflow: hidden;
    background: var(--white);
  }
  .slide {
    position: relative;
    width: 1200px;
    height: 900px;
    overflow: hidden;
    background: var(--white);
  }
  .texture {
    position: absolute;
    right: 0;
    top: 0;
    width: 620px;
    height: 700px;
    background: radial-gradient(ellipse at 100% 45%, var(--dots) 0%, rgba(230,230,230,0.5) 35%, rgba(255,255,255,0) 70%);
  }
  .title-panel {
    position: absolute;
    left: 0;
    top: 36px;
    width: 1152px;
    height: 537px;
    background: var(--lime);
    border-radius: 0 24px 24px 0;
  }
  .project-title {
    position: absolute;
    right: 48px;
    top: 238px;
    margin: 0;
    font-family: "Ubuntu", sans-serif;
    font-weight: 400;
    font-size: 43px;
    line-height: 1;
    color: var(--white);
  }
  .project-subtitle {
    position: absolute;
    right: 52px;
    top: 330px;
    margin: 0;
    width: 620px;
    text-align: right;
    font-family: "Carlito", sans-serif;
    font-size: 21px;
    line-height: 33px;
    color: var(--ink);
  }
  .brand {
    position: absolute;
    left: 771px;
    top: 696px;
    display: flex;
    align-items: center;
    gap: 34px;
  }
  .brand-mark {
    width: 48px;
    height: 48px;
    border-radius: 50%;
    background: var(--lime);
  }
  .brand-name {
    font-family: "Ubuntu", sans-serif;
    font-weight: 700;
    font-size: 54px;
    letter-spacing: 6px;
    line-height: 1;
    color: var(--brand-grey);
  }
  .footer {
    position: absolute;
    left: 0;
    bottom: 0;
    width: 1200px;
    height: 57px;
    border-top: 1px solid var(--footer-line);
    background: linear-gradient(var(--footer-top), var(--footer-bottom));
    display: flex;
    align-items: center;
    justify-content: space-between;
    padding: 0 52px 0 36px;
    box-sizing: border-box;
    font-family: "Roboto Condensed", sans-serif;
    font-weight: 700;
    font-size: 21px;
    color: var(--ink);
  }
</style>
</head>
<body>
  <main class="slide">
    <div class="texture" role="img" aria-label="Soft grey dotted pattern fading in from the right edge"></div>
    <section class="title-panel">
      <h1 class="project-title">Project Title Here</h1>
      <p class="project-subtitle">Sub text here Sub text here Sub text here Sub text here<br>Sub text here Sub text here Sub text here Sub</p>
    </section>
    <div class="brand">
      <span class="brand-mark"></span>
      <span class="brand-name">TOLVARE</span>
    </div>
    <footer class="footer">
      <span class="page-number">Page No. 00</span>
      <span class="copyright">Copyright@2013</span>
    </footer>
  </main>
</body>
</html>
```